Harbo Hale - A non profit for healthy lifestyle and fitness within refugee camps

We need a logo and website design for a new 501c3 Non-Profit based in San Francisco called 'Harbo Hale'. We help coordinate trips across the globe to provide fitness classes to refugee camps to help refugees maintain a healthy lifestyle and fun while exercising.
Our first trip was to Greece and we hope to extend our reach by working with other non-profits to coordinate how we can help bring a healthy lifestyle and a wellness to refugees in need.
We would like to see website design that use the color green and blue. The final design should represent a welcoming website to encourage people to take a trip either by themselves, as a group, or with a corporate team.
We have 3 certified and experienced trainers that will be running these trips and with a hope of 20 volunteers per trip to help.

We are hoping to partner with another 501c3 called 'Tide to Dawn' which I have participated in and with the hopes of providing an easier and simpler user experience than their current website but with many of the same content.

We would like a 'Trips' page with previous trips, 'Trainers/Hosts' page with bios of the leaders hosting the event, 'Register Page' for folks to register for upcoming trips, 'About Us' page for our mission statement and work, 'Albums' page for photos taken on the trip, 'Contact Us' page for FAQs and questions to submit, and a 'Donate' page for people to donate to our cause.

I would like this page to be created in Word Press.

ie: http://www.tidetodawn-example.com.au/programs/

Target Market(s)

Volunteers, non-profit partners

Industry/Entity Type

Non-Profit

Number of Pages Required

4 page

Font styles to use
Sans Serif

Colors

Designer to choose colors to be used in the design.

Requirements
Must have
• 'Trips' page with previous trips, 'Trainers/Hosts' page with bios of the leaders hosting the event, 'Register Page' for folks to register for upcoming trips, 'About Us' page for our mission statement and work, 'Albums' page for photos taken on the trip, 'Contact Us' page for FAQs and questions to submit, and a 'Donate' page for people to donate to our cause.

```html
<!DOCTYPE html>
<html lang="en">
<head>
<meta charset="utf-8">
<title>Harbo Hale — Community Foundation</title>
<link href="https://fonts.googleapis.com/css2?family=Montserrat:wght@400;600;700;800&family=Open+Sans:wght@400;600;700&display=swap" rel="stylesheet">
<style>
:root{
  --blue:#1b8fd8;
  --blue-deep:#0b5ea6;
  --navy:#0b3a66;
  --navy-dark:#082c4f;
  --green:#6dbb45;
  --green-dark:#5aa636;
  --ink:#1d1d1d;
  --grey:#666;
  --light:#f1f1f1;
  --line:#e2e2e2;
  --white:#fff;
}
*{box-sizing:border-box;margin:0;padding:0}
html,body{width:1200px;height:3593px;overflow:hidden}
body{font-family:'Open Sans',Arial,sans-serif;color:var(--ink);background:var(--white);position:relative}
.h{font-family:'Montserrat',Arial,sans-serif}
section,header,footer{position:absolute;left:0;width:1200px}
.wrap{position:absolute;left:170px;width:860px}
.fill{position:absolute}

/* top bar */
.topbar{top:0;height:36px;background:#fff;border-bottom:1px solid var(--line);font-size:11px;color:var(--grey)}
.topbar .info{position:absolute;left:170px;top:0;height:36px;display:flex;align-items:center;gap:34px}
.topbar .info span{display:flex;align-items:center;gap:7px}
.topbar .social{position:absolute;left:768px;top:8px;display:flex;gap:7px}
.topbar .social i{width:20px;height:20px;border-radius:50%;border:1.5px solid var(--navy);display:block}
.topbar .donate-now{position:absolute;left:917px;top:0;width:110px;height:36px;background:var(--green);color:#fff;font:700 11px 'Montserrat',sans-serif;display:flex;align-items:center;justify-content:center;gap:6px}

/* nav */
.nav{top:36px;height:72px;background:linear-gradient(#fff,#f3f3f3);box-shadow:0 2px 4px rgba(0,0,0,.12);z-index:3}
.brand{position:absolute;left:170px;top:15px;font:800 34px 'Montserrat',sans-serif;color:var(--blue);letter-spacing:-.5px}
.menu{position:absolute;left:420px;top:0;height:72px;display:flex;align-items:center;gap:25px;font-size:13px;color:#555}

/* hero */
.hero{top:108px;height:467px;background:radial-gradient(ellipse at 25% 40%,#4a4a4a 0%,#1a1a1a 45%,#050505 80%)}
.hero-text{position:absolute;left:596px;top:92px;color:#fff}
.hero-text .kicker{font:700 22px 'Montserrat',sans-serif}
.hero-text .welcome{font:800 56px/1 'Montserrat',sans-serif;margin-top:10px}
.hero-text .name{font:800 64px/1 'Montserrat',sans-serif;color:var(--blue);margin-top:4px}
.btn{display:inline-flex;align-items:center;gap:10px;background:var(--green);color:#fff;font-family:'Montserrat',sans-serif;font-weight:700;border-radius:3px}
.hero .btn{position:absolute;left:597px;top:288px;height:66px;padding:0 24px;font-size:20px}
.dots{display:flex;gap:6px}
.dots i{width:11px;height:11px;border-radius:50%;border:2px solid #fff;display:block}
.dots i.on{background:#fff}
.hero .dots{position:absolute;left:600px;top:377px}

/* help */
.help{top:575px;height:388px;background:#efefef}
.sec-title{position:absolute;left:0;width:1200px;text-align:center;font:800 30px 'Montserrat',sans-serif;color:var(--ink)}
.sec-title em{font-style:normal;color:var(--green)}
.help .sec-title{top:44px}
.cards{position:absolute;left:170px;top:120px;display:flex;gap:24px}
.card{width:196px;height:196px;background:#fff;box-shadow:0 2px 6px rgba(0,0,0,.18);display:flex;flex-direction:column;align-items:center;justify-content:center;gap:18px;font:700 12px 'Montserrat',sans-serif;color:var(--blue);text-align:center}
.card.text{justify-content:flex-start;padding-top:36px;gap:8px}
.card.text p{font:400 11px/1.5 'Open Sans',sans-serif;color:#666;width:150px}
.plus{width:28px;height:28px;border-radius:50%;background:var(--green);color:#fff;font:700 22px/28px 'Open Sans',sans-serif;margin-top:6px}

/* team */
.team{top:963px;height:431px;background:linear-gradient(135deg,#0f6fbc,#0b4f90)}
.team .photo{left:0;top:0;width:600px;height:431px;background:linear-gradient(180deg,#1e7cc6 0%,#2b8ed4 50%,#1766a8 100%)}
.team-text{position:absolute;left:615px;top:70px;width:410px;color:#fff}
.team-text h2{font:800 28px 'Montserrat',sans-serif}
.team-text h2 em{font-style:normal;color:var(--green)}
.team-text p{font-size:12.5px;line-height:1.6;margin-top:16px}
.stats{display:flex;gap:28px;margin-top:22px}
.stat{display:flex;gap:8px;align-items:center}
.stat small{display:block;font-size:11px}
.stat b{font:700 18px 'Montserrat',sans-serif}
.team .btn{margin-top:24px;height:48px;padding:0 26px;font-size:13px}

/* trips */
.trips{top:1394px;height:709px;background:#fff}
.trips .sec-title{top:60px}
.bar{position:absolute;left:570px;width:60px;height:3px;background:var(--green)}
.trip{position:absolute;left:170px;width:544px;border:1px solid var(--line);box-shadow:0 1px 4px rgba(0,0,0,.08);background:#fff}
.trip .date{position:absolute;left:10px;top:30px;width:78px;height:74px;border:1px solid var(--line);text-align:center;color:var(--blue)}
.trip .date b{display:block;font:800 34px/1.2 'Montserrat',sans-serif}
.trip .date small{font:700 11px 'Montserrat',sans-serif;color:#333}
.trip .thumb{left:86px;top:0;width:160px;height:132px}
.trip .meta{position:absolute;left:266px;top:28px;font-size:10.5px;color:#555;line-height:1}
.trip .meta h3{font:700 14px 'Montserrat',sans-serif;color:var(--blue);margin-bottom:16px}
.trip .meta div{display:flex;align-items:center;gap:8px;margin-bottom:12px}
.trip p{position:absolute;left:76px;top:146px;width:446px;font-size:11px;line-height:1.6;color:#555}
.promo{position:absolute;left:738px;top:139px;width:289px;height:527px;background:linear-gradient(160deg,#3a3a3a,#161616 60%,#0a0a0a)}
.promo-text{position:absolute;left:28px;top:160px;width:240px;color:#fff}
.promo-text h3{font:700 34px 'Montserrat',sans-serif;color:var(--green)}
.promo-text h4{font:700 14px 'Montserrat',sans-serif;margin-top:4px}
.promo-text .when{font:700 13px 'Open Sans',sans-serif;margin-top:24px}
.promo-text p{font-size:12px;line-height:1.55;margin-top:16px}
.promo .btn{margin-top:16px;height:36px;padding:0 18px;font-size:11px}
.trips .dots{position:absolute;left:420px;top:624px}
.trips .dots i{border-color:var(--blue);width:10px;height:10px}
.trips .dots i.on{background:var(--blue)}

/* video */
.video{top:2103px;height:404px;background:linear-gradient(90deg,#0a3a66 0%,#1a5c96 25%,#0f3f72 55%,#1c4f85 100%)}
.notch{position:absolute;left:560px;top:0}
.video-text{position:absolute;left:0;top:112px;width:1200px;text-align:center;color:#fff}
.video-text h3{font:700 27px 'Montserrat',sans-serif}
.video-text h2{font:800 60px 'Montserrat',sans-serif;color:var(--green);margin-top:2px}
.play{position:absolute;left:560px;top:248px}

/* albums */
.albums{top:2507px;height:487px;background:var(--green)}
.albums .sec-title{top:46px;color:#1d1d1d}
.albums .sec-title em{color:#fff}
.gallery{position:absolute;left:0;top:120px;width:1200px;height:276px;display:flex;gap:6px;background:#fff}
.gallery > div{flex:1;position:relative}
.gallery .over{position:absolute;left:0;top:0;width:100%;height:100%;display:flex;flex-direction:column;align-items:center;justify-content:center;gap:10px;color:#fff;font:600 22px 'Montserrat',sans-serif;background:rgba(0,0,0,.35)}
.albums .pager{position:absolute;left:0;top:424px;width:1200px;display:flex;justify-content:center;align-items:center;gap:14px;color:#111;font-size:14px}
.albums .pager i{width:7px;height:7px;border-radius:50%;background:#111;display:block}
.albums .pager i.on{background:#fff}

/* contact strip */
.contact{top:2994px;height:251px;background:#f4f4f4}
.cbox{position:absolute;top:0;height:251px;display:flex;flex-direction:column;align-items:center;justify-content:center;gap:18px;text-align:center;font-size:15px;line-height:1.45;color:#333}
.chev{position:absolute;top:0}

/* footer */
.footer{top:3245px;height:288px;background:var(--navy);color:#fff}
.col{position:absolute;top:42px}
.col h4{font:600 17px 'Montserrat',sans-serif;margin-bottom:20px}
.col .brand-foot{font:800 40px 'Montserrat',sans-serif;color:var(--blue);line-height:1;margin-bottom:14px}
.col p{font-size:11px;line-height:1.6;width:210px}
.links{list-style:none;font-size:11.5px}
.links li{display:flex;align-items:center;gap:12px;margin-bottom:6px}
.links li i{width:11px;height:11px;border-radius:50%;border:1.5px solid var(--green);display:block}
.thumbs{display:grid;grid-template-columns:repeat(3,52px);gap:8px}
.thumbs span{height:44px;display:block}
.citem{display:flex;align-items:center;gap:14px;font-size:11px;margin-bottom:14px;line-height:1.4}
.fsocial{display:flex;gap:6px;margin-top:6px}
.fsocial i{width:28px;height:28px;border-radius:50%;border:1.5px solid #fff;display:block}
.totop{position:absolute;left:1125px;top:190px;width:40px;text-align:center;font-size:9px;color:var(--green);line-height:1.2}
.copy{top:3533px;height:60px;background:var(--navy-dark);color:#cfd8e3;font-size:11px;display:flex;align-items:center;justify-content:center}
</style>
</head>
<body>

<header class="topbar">
  <div class="info">
    <span><svg width="12" height="12" viewBox="0 0 24 24" fill="#0b3a66"><path d="M6.6 10.8a15 15 0 0 0 6.6 6.6l2.2-2.2a1 1 0 0 1 1-.25 11 11 0 0 0 3.6.6 1 1 0 0 1 1 1V20a1 1 0 0 1-1 1A17 17 0 0 1 3 4a1 1 0 0 1 1-1h3.5a1 1 0 0 1 1 1c0 1.25.2 2.45.6 3.6a1 1 0 0 1-.25 1z"/></svg>Call us: 123-456-7890</span>
    <span><svg width="13" height="10" viewBox="0 0 26 20" fill="#0b3a66"><path d="M0 0h26v20H0z M2 2v1l11 8 11-8V2z" fill-rule="evenodd"/></svg>E-mail: info@harbohale.org</span>
  </div>
  <div class="social"><i></i><i></i><i></i><i></i></div>
  <div class="donate-now"><svg width="12" height="11" viewBox="0 0 24 22" fill="#fff"><path d="M12 22 2 12A6 6 0 0 1 12 4a6 6 0 0 1 10 8z"/></svg>DONATE NOW</div>
</header>

<header class="nav">
  <div class="brand">Harbo Hale</div>
  <nav class="menu">
    <svg width="22" height="20" viewBox="0 0 24 22" fill="#1b8fd8"><path d="M12 0 0 11h3v11h7v-7h4v7h7V11h3z"/></svg>
    <span>Trips</span><span>Trainers/Hosts</span><span>Register</span><span>About Us</span><span>Albums</span><span>Contact Us</span><span>Donate</span>
    <svg width="16" height="16" viewBox="0 0 24 24" fill="none" stroke="#0b3a66" stroke-width="3"><circle cx="10" cy="10" r="7"/><path d="m15 15 7 7"/></svg>
  </nav>
</header>

<section class="hero" role="img" aria-label="Black and white photo of a cyclist riding a road bike">
  <div class="hero-text">
    <div class="kicker">Community Foundation</div>
    <div class="welcome">WELCOME TO</div>
    <div class="name">HARBO HALE</div>
  </div>
  <div class="btn">How you can Help? <svg width="20" height="20" viewBox="0 0 24 24"><circle cx="12" cy="12" r="11" fill="#fff"/><path d="M9 7l5 5-5 5" stroke="#6dbb45" stroke-width="3" fill="none"/></svg></div>
  <div class="dots"><i class="on"></i><i></i><i></i></div>
</section>

<section class="help">
  <h2 class="sec-title">HOW COULD YOU <em>HELP?</em></h2>
  <div class="cards">
    <div class="card text">GIVE INSPIRATION<p>Lorem Ipsum is simply dummy text of the printing and typesetting industry. Lorem Ipsum has been</p><div class="plus">+</div></div>
    <div class="card"><svg width="52" height="60" viewBox="0 0 52 60" fill="none" stroke="#6dbb45" stroke-width="3.5" stroke-linejoin="round"><path d="M10 30V12a4 4 0 0 1 8 0v14V6a4 4 0 0 1 8 0v20V8a4 4 0 0 1 8 0v18-12a4 4 0 0 1 8 0v24c0 12-8 18-17 18S8 52 4 42l-2-6a4 4 0 0 1 8-4z"/><path d="M26 40l-6-6a3.5 3.5 0 0 1 6-3 3.5 3.5 0 0 1 6 3z" fill="#6dbb45"/></svg>BECOME VOLUNTEER</div>
    <div class="card"><svg width="64" height="56" viewBox="0 0 64 56" fill="#6dbb45"><circle cx="44" cy="7" r="6"/><path d="M30 14h14l6 12 10 2-1 4-13-3-4-6-5 10 8 8-4 14h-5l3-11-9-7-4 8-14-2 1-4 10 1 7-17h-6l-5 7-4-2z"/><rect x="0" y="18" width="16" height="3"/><rect x="4" y="26" width="14" height="3"/><rect x="0" y="34" width="12" height="3"/></svg>RUFEGEE FITNESS</div>
    <div class="card"><svg width="56" height="62" viewBox="0 0 56 62" fill="#6dbb45"><rect x="8" y="34" width="40" height="26"/><rect x="22" y="34" width="12" height="4" fill="#fff"/><path d="M14 28 28 6c3-4 10-2 8 4l-4 8h14c3 0 4 3 2 5l-6 5z"/><circle cx="28" cy="46" r="4" fill="#fff"/></svg>SEND DONATION</div>
  </div>
</section>

<section class="team">
  <div class="fill photo" role="img" aria-label="Photo of five smiling volunteers in matching grey t-shirts"></div>
  <div class="team-text">
    <h2>WE ARE <em>NONPROFIT TEAM</em></h2>
    <p>Lorem Ipsum is simply dummy text of the printing and typesetting industry. Lorem Ipsum has been the industry's standard dummy text ever since the 1500s, when an unknown printer took a galley of type and scrambled it to make a type specimen book.</p>
    <div class="stats">
      <div class="stat"><svg width="26" height="22" viewBox="0 0 26 22" fill="#6dbb45"><rect x="0" y="10" width="5" height="12"/><path d="M7 10h6l4 3h6a3 3 0 0 1 0 5H7z"/><circle cx="18" cy="5" r="5"/></svg><div><small>Donation</small><b>1500+</b></div></div>
      <div class="stat"><svg width="22" height="26" viewBox="0 0 22 26" fill="#6dbb45"><path d="M3 14V6a2 2 0 0 1 4 0v6V3a2 2 0 0 1 4 0v9V4a2 2 0 0 1 4 0v8-4a2 2 0 0 1 4 0v10c0 5-4 8-8 8s-8-3-10-7l-1-3a2 2 0 0 1 3-2z"/></svg><div><small>Helped People</small><b>3500+</b></div></div>
      <div class="stat"><svg width="26" height="24" viewBox="0 0 26 24" fill="#6dbb45"><circle cx="13" cy="6" r="5"/><path d="M3 24c0-7 4-11 10-11s10 4 10 11z"/></svg><div><small>Volunteers</small><b>500+</b></div></div>
    </div>
    <div class="btn">READ MORE <svg width="16" height="16" viewBox="0 0 24 24"><circle cx="12" cy="12" r="11" fill="#fff"/><path d="M9 7l5 5-5 5" stroke="#6dbb45" stroke-width="3" fill="none"/></svg></div>
  </div>
</section>

<section class="trips">
  <h2 class="sec-title">LATEST <em>TRIPS</em></h2>
  <div class="bar" style="top:112px"></div>

  <article class="trip" style="top:139px;height:227px">
    <div class="date"><b>23</b><small>DEC-2017</small></div>
    <div class="fill thumb" role="img" aria-label="Photo of a runner silhouetted against a golden sunset" style="background:linear-gradient(180deg,#f0a32c,#b8620f 70%,#3b2208);left:86px;top:0"></div>
    <div class="meta">
      <h3>Fitness Charity Event 2017</h3>
      <div><svg width="10" height="10" viewBox="0 0 24 24" fill="#6dbb45"><circle cx="12" cy="12" r="11"/></svg>Dec 23, 2017 09:00 AM to Dec 24, 2017 1:00 PM</div>
      <div><svg width="10" height="12" viewBox="0 0 20 26" fill="#6dbb45"><path d="M10 0a9 9 0 0 0-9 9c0 7 9 17 9 17s9-10 9-17a9 9 0 0 0-9-9zm0 13a4 4 0 1 1 0-8 4 4 0 0 1 0 8z"/></svg>Greece</div>
      <div><svg width="10" height="10" viewBox="0 0 24 24" fill="#6dbb45"><circle cx="12" cy="12" r="11"/></svg>$100</div>
    </div>
    <p>Lorem ipsum dolor sit amet, consectetur adipiscing elit, sed do eiusmod tempor incididunt ut labore et dolore magna aliqua. Ut enim ad minim veniam, quis nostrud exercitation ullamco laboris nisi ut aliquip ex ea commodo consequat.</p>
  </article>

  <article class="trip" style="top:407px;height:194px">
    <div class="date"><b>23</b><small>DEC-2017</small></div>
    <div class="fill thumb" role="img" aria-label="Photo of cupped hands holding coins" style="background:radial-gradient(circle at 50% 50%,#c08a3a,#5a3a1a 55%,#1a120a);left:86px;top:0;height:132px"></div>
    <div class="meta">
      <h3>Fitness Charity Event 2017</h3>
      <div><svg width="10" height="10" viewBox="0 0 24 24" fill="#6dbb45"><circle cx="12" cy="12" r="11"/></svg>Dec 23, 2017 09:00 AM to Dec 24, 2017 1:00 PM</div>
      <div><svg width="10" height="12" viewBox="0 0 20 26" fill="#6dbb45"><path d="M10 0a9 9 0 0 0-9 9c0 7 9 17 9 17s9-10 9-17a9 9 0 0 0-9-9zm0 13a4 4 0 1 1 0-8 4 4 0 0 1 0 8z"/></svg>Greece</div>
      <div><svg width="10" height="10" viewBox="0 0 24 24" fill="#6dbb45"><circle cx="12" cy="12" r="11"/></svg>$100</div>
    </div>
    <p style="top:140px">Lorem ipsum dolor sit amet, consectetur adipiscing elit, sed do eiusmod tempor incididunt ut labore et dolore magna aliqua. Ut enim ad minim veniam, quis nostrud exercitation ullamco laboris nisi ut aliquip ex ea commodo consequat.</p>
  </article>

  <aside class="promo" role="img" aria-label="Black and white photo of a child looking up">
    <div class="promo-text">
      <h3>GIVE A HAND</h3>
      <h4>FOR THESE CHILDREN'S FUTURE</h4>
      <div class="when">December 24, 2016 / Brazil Park</div>
      <p>Lorem ipsum dolor sit amet, consectetur ipui lore adipisicing elit, sed do eiusmod.</p>
      <div class="btn">READ MORE <svg width="14" height="14" viewBox="0 0 24 24"><circle cx="12" cy="12" r="11" fill="#fff"/><path d="M9 7l5 5-5 5" stroke="#6dbb45" stroke-width="3" fill="none"/></svg></div>
    </div>
  </aside>

  <div class="dots"><i class="on"></i><i></i><i></i></div>
</section>

<section class="video" role="img" aria-label="Blue-toned photo of a thoughtful man and a cyclist silhouetted at dusk">
  <svg class="notch" width="80" height="34" viewBox="0 0 80 34"><path d="M0 0h80c-14 0-20 34-40 34S14 0 0 0z" fill="#fff"/><path d="M33 12l7 7 7-7" stroke="#1b8fd8" stroke-width="3" fill="none"/></svg>
  <div class="video-text">
    <h3>Save The Life To Make The Better World</h3>
    <h2>BECAUSE YOU CAN</h2>
  </div>
  <svg class="play" width="80" height="80" viewBox="0 0 80 80"><circle cx="40" cy="40" r="38" fill="#1b8fd8"/><path d="M32 24l24 16-24 16z" fill="#0b3a66"/></svg>
</section>

<section class="albums">
  <h2 class="sec-title">OUR <em>ALBUMS</em></h2>
  <div class="gallery">
    <div role="img" aria-label="Photo of a cyclist silhouetted at sunset" style="background:linear-gradient(180deg,#223a55,#111c2a 60%,#b55a1c)">
      <div class="over"><svg width="28" height="18" viewBox="0 0 28 18" fill="none" stroke="#6dbb45" stroke-width="2.5"><path d="M1 9s5-8 13-8 13 8 13 8-5 8-13 8S1 9 1 9z"/><circle cx="14" cy="9" r="3.5"/></svg>LOREM IPSUM<svg width="24" height="24" viewBox="0 0 24 24" fill="none" stroke="#fff" stroke-width="2.5"><path d="M10 14a5 5 0 0 0 7 0l4-4a5 5 0 0 0-7-7l-1 1M14 10a5 5 0 0 0-7 0l-4 4a5 5 0 0 0 7 7l1-1"/></svg></div>
    </div>
    <div role="img" aria-label="Black and white photo of a road cyclist" style="background:radial-gradient(circle at 50% 40%,#5a5a5a,#151515 70%)"></div>
    <div role="img" aria-label="Black and white portrait of a child" style="background:radial-gradient(circle at 50% 50%,#8a8a8a,#3a3a3a 70%)"></div>
    <div role="img" aria-label="Photo of cupped hands holding coins" style="background:radial-gradient(circle at 50% 55%,#b5833e,#4d3219 55%,#141008)"></div>
  </div>
  <div class="pager">‹ <i></i><i class="on"></i><i></i><i></i> ›</div>
</section>

<section class="contact">
  <svg class="chev" style="left:0" width="1200" height="251" viewBox="0 0 1200 251">
    <path d="M0 0h370l48 125-48 126H0z" fill="#f7f7f7"/>
    <path d="M370 0h410l48 125-48 126H370l48-126z" fill="#ededed"/>
    <path d="M780 0h420v251H780l48-126z" fill="#f5f5f5"/>
  </svg>
  <div class="cbox" style="left:60px;width:290px">
    <svg width="44" height="58" viewBox="0 0 44 58" fill="none" stroke="#1b8fd8" stroke-width="2.5"><path d="M22 2a17 17 0 0 0-17 17c0 13 17 33 17 33s17-20 17-33A17 17 0 0 0 22 2z"/><circle cx="22" cy="19" r="6"/><path d="M6 56h32"/></svg>
    <div>Address Goes Here<br>text of the printing and<br>typesetting industry.</div>
  </div>
  <div class="cbox" style="left:450px;width:300px">
    <svg width="52" height="52" viewBox="0 0 24 24" fill="none" stroke="#1b8fd8" stroke-width="1.2"><path d="M6.6 10.8a15 15 0 0 0 6.6 6.6l2.2-2.2a1 1 0 0 1 1-.25 11 11 0 0 0 3.6.6 1 1 0 0 1 1 1V20a1 1 0 0 1-1 1A17 17 0 0 1 3 4a1 1 0 0 1 1-1h3.5a1 1 0 0 1 1 1c0 1.25.2 2.45.6 3.6a1 1 0 0 1-.25 1z"/></svg>
    <div>+123 456 7890 - Office<br>(123) 456 7890 - Fax</div>
  </div>
  <div class="cbox" style="left:870px;width:300px">
    <svg width="58" height="52" viewBox="0 0 58 52" fill="none" stroke="#1b8fd8" stroke-width="2.5" stroke-linejoin="round"><path d="M2 22 56 2 46 48 28 36z"/><path d="M56 2 28 36v14l8-10"/></svg>
    <div>support@harbohale.org<br>hello@harbohale.org</div>
  </div>
</section>

<footer class="footer">
  <div class="col" style="left:170px">
    <h4>About Company</h4>
    <div class="brand-foot">Harbo Hale</div>
    <p>Lorem Ipsum is simply dummy text of the printing and typesetting industry. Lorem Ipsum has been the industry's standard dummy text ever since the 1500s, when an unknown printer took a galley of type and scrambled it to make a type specimen book.</p>
  </div>
  <div class="col" style="left:438px">
    <h4>Quick Links</h4>
    <ul class="links">
      <li><i></i>Home</li><li><i></i>Trips</li><li><i></i>Trainers/Hosts</li><li><i></i>Register</li><li><i></i>About Us</li><li><i></i>Albums</li><li><i></i>Contact Us</li><li><i></i>Donate</li>
    </ul>
  </div>
  <div class="col" style="left:644px">
    <h4>Our Albums</h4>
    <div class="thumbs" role="img" aria-label="Thumbnails of trip photos">
      <span style="background:#6b4b2e"></span><span style="background:#8a6a4a"></span><span style="background:#4a3a2a"></span>
      <span style="background:#7a5a3a"></span><span style="background:#3a4a5a"></span><span style="background:#a07a4a"></span>
      <span style="background:#5a4030"></span><span style="background:#8a7050"></span><span style="background:#4a5a6a"></span>
    </div>
  </div>
  <div class="col" style="left:884px">
    <h4>Contact Us</h4>
    <div class="citem"><svg width="12" height="15" viewBox="0 0 20 26" fill="#fff"><path d="M10 0a9 9 0 0 0-9 9c0 7 9 17 9 17s9-10 9-17a9 9 0 0 0-9-9zm0 13a4 4 0 1 1 0-8 4 4 0 0 1 0 8z"/></svg>Address Goes Here</div>
    <div class="citem"><svg width="13" height="10" viewBox="0 0 26 20" fill="#fff"><path d="M0 0h26v20H0z M2 2v1l11 8 11-8V2z" fill-rule="evenodd"/></svg>info@harbohale.org</div>
    <div class="citem"><svg width="12" height="12" viewBox="0 0 24 24" fill="#fff"><path d="M6.6 10.8a15 15 0 0 0 6.6 6.6l2.2-2.2a1 1 0 0 1 1-.25 11 11 0 0 0 3.6.6 1 1 0 0 1 1 1V20a1 1 0 0 1-1 1A17 17 0 0 1 3 4a1 1 0 0 1 1-1h3.5a1 1 0 0 1 1 1c0 1.25.2 2.45.6 3.6a1 1 0 0 1-.25 1z"/></svg><span>+123 456 7890<br>+123 456 7890</span></div>
    <div class="fsocial"><i></i><i></i><i></i><i></i></div>
  </div>
  <div class="totop"><svg width="22" height="30" viewBox="0 0 22 30" fill="none" stroke="#6dbb45" stroke-width="2"><path d="M11 1c6 5 7 14 4 20H7C4 15 5 6 11 1z"/><circle cx="11" cy="11" r="2.5"/><path d="M7 21l-4 5 5-1M15 21l4 5-5-1"/></svg><br>back to<br>top</div>
</footer>

<div class="copy" style="position:absolute;left:0;top:3533px;width:1200px">Copyright @ 2017 | Harbo Hale | All Rights Reserved</div>

</body>
</html>
```